Letterhead for Midwest Law Firm

Our law firm does estate planning and trust administration in Wisconsin and Illinois. We recently obtained a new logo and need to incorporate it into new stationary. The stationary needs to list out the attorneys at the firm, but we will want 3 variations, one with three attorneys, one with six, and one with six plus the names of states where each is licensed to practice (possibly as an asterisk with notation somewhere towards bottom of page. As with most traditional law practices, letterhead should be conservative and convey predictability and reliability. We view our brand as being primarily reliability, with prestige as a secondary element. We are upmarket, but would like to avoid seeming pretentious or "slick". We are a smaller firm with a personal touch.

Target Market(s)

Affluent Midwestern Americans approaching at or approaching retirement age.

Industry/Entity Type

Legal

Font styles to use
Serif
Sans Serif

Requirements
Must have
• Must use our logo. Must comply with Northgate Counsel Guild Ethics rules: https://www.quarvenlex.org/rules/offices/docs/plmtk41annotated.pdf. Must be conventional. Must list names of attorneys and provide contact information for firm. Note that we are asking for three designs with very minor variations. Also, designer must provide letterhead in a format that is industry-standard for stationary printers.
Nice to have
• We would appreciate an alternate version that will look reasonable when printed on a black-and-white printer. Designer can use judgment as to whether to have use grayscale, black/white, or something in between.
Should not have
• No "motto" or "visit our website" extraneous materials. putting the website address somewhere is fine, but overall there is a lot of required text, and we'd like to not appear cluttered.

```html
<!DOCTYPE html>
<html lang="en">
<head>
<meta charset="utf-8">
<title>Hallbrook &amp; Vane LLP — Letterhead</title>
<link href="https://fonts.googleapis.com/css2?family=Didact+Gothic&family=Libre+Baskerville&display=swap" rel="stylesheet">
<style>
  :root {
    --backdrop: #e4e4e2;
    --paper: #f3f3f3;
    --ink: #2b2b2b;
    --ink-soft: #555555;
    --brand: #6a6a6a;
    --rule: #9a9a9a;
    --band: #3b3b3b;
    --icon: #333333;
  }
  * { margin: 0; padding: 0; box-sizing: border-box; }
  html, body {
    width: 1200px; height: 799px; overflow: hidden;
    background: var(--backdrop);
  }
  .sheet {
    position: absolute; left: 361px; top: 60px;
    width: 478px; height: 678px;
    background: var(--paper);
    font-family: "Didact Gothic", "Century Gothic", sans-serif;
    color: var(--ink);
  }
  .brand {
    position: absolute; left: 0; right: 0; top: 30px;
    text-align: center;
    font-family: "Libre Baskerville", Georgia, serif;
    color: var(--brand);
  }
  .brand-mark {
    width: 12px; height: 12px; margin: 0 auto 6px;
    border: 1.5px solid var(--brand); border-radius: 50%;
  }
  .brand-name { font-size: 11px; letter-spacing: .2px; line-height: 1.3; }
  .brand-suffix { font-size: 6.5px; letter-spacing: 1px; }
  .letter {
    position: absolute; left: 58px; top: 175px; width: 365px;
    font-size: 8.8px; line-height: 10.7px;
  }
  .letter p { margin-bottom: 10.5px; }
  .letter .body { text-align: justify; }
  .signature {
    position: absolute; left: 333px; top: 425px; width: 95px; height: 73px;
    background: linear-gradient(135deg, #ececec, #e6e6e6);
    border-radius: 4px;
  }
  .footer {
    position: absolute; left: 58px; top: 620px; width: 390px; height: 29px;
    border-top: 1px solid var(--rule); border-bottom: 1px solid var(--rule);
    font-size: 6.5px; line-height: 8.4px;
  }
  .footer .item { position: absolute; top: 6px; }
  .attorneys { left: 0; font-weight: bold; color: var(--ink); font-family: "Didact Gothic", Arial, sans-serif; -webkit-text-stroke: .25px var(--ink); }
  .contact { color: var(--ink-soft); }
  .email { left: 158px; }
  .phone { left: 252px; }
  .web { left: 334px; }
  .icon { position: absolute; top: 8px; width: 13px; height: 13px; }
  .icon-email { left: 135px; }
  .icon-phone { left: 229px; }
  .icon-web { left: 309px; }
  .band {
    position: absolute; left: 0; bottom: 0; width: 100%; height: 9px;
    background: var(--band);
  }
</style>
</head>
<body>
  <main class="sheet">
    <header class="brand">
      <div class="brand-mark"></div>
      <div class="brand-name">Hallbrook &amp; Vane</div>
      <div class="brand-suffix">LLP</div>
    </header>

    <section class="letter">
      <p>2210, Larkmoor Avenue<br>Fairhaven, CA 90412.</p>
      <p>January 29th, 2011</p>
      <p>Mr. Delmont<br>President, Delmont Youth Center<br>517 Orchard Row<br>Brookfield, NY 10488</p>
      <p>Dear Mr. Delmont:</p>
      <p class="body">In the first paragraph, one needs to give a brief introduction of oneself. One should also give reference to the purpose of the letter in brief.The second paragraph needs to give the details of the letter and its need. This paragraph is mostly longer than the others and plays the main role in the letter. Keep the sentences short and to the point. Avoid using complex words and sentences.</p>
      <p>The third and last paragraph is the conclusion of the letter and can be kept short.</p>
      <p>Sincerely,</p>
      <p>(this is where the signature of the writer will be placed)</p>
      <p>Morgan Ellery</p>
    </section>

    <div class="signature" role="img" aria-label="Handwritten signature of the letter writer"></div>

    <footer class="footer">
      <div class="item attorneys">Barlow, Celia R. CC - Ashford<br>Corwin, Joan T. CC - Linden</div>

      <svg class="icon icon-email" viewBox="0 0 14 14" aria-hidden="true">
        <circle cx="7" cy="7" r="7" fill="var(--icon)"/>
        <rect x="3.6" y="4.8" width="6.8" height="4.6" fill="none" stroke="#fff" stroke-width=".9"/>
        <path d="M3.6 4.8 L7 7.4 L10.4 4.8" fill="none" stroke="#fff" stroke-width=".9"/>
      </svg>
      <div class="item contact email">office@hallbrookvane.org<br>office@hallbrookvane.org</div>

      <svg class="icon icon-phone" viewBox="0 0 14 14" aria-hidden="true">
        <circle cx="7" cy="7" r="7" fill="var(--icon)"/>
        <path d="M4.4 3.8 L5.8 3.6 L6.4 5.4 L5.6 6.1 Q6.4 7.7 7.9 8.4 L8.6 7.6 L10.4 8.2 L10.2 9.6 Q9.6 10.4 8.4 10.2 Q4.2 9 3.8 5 Q3.7 4.2 4.4 3.8 Z" fill="#fff"/>
      </svg>
      <div class="item contact phone">(555) 318-4402<br>(555) 318-4417</div>

      <svg class="icon icon-web" viewBox="0 0 14 14" aria-hidden="true">
        <circle cx="7" cy="7" r="7" fill="var(--icon)"/>
        <circle cx="7" cy="7" r="3.4" fill="none" stroke="#fff" stroke-width=".8"/>
        <ellipse cx="7" cy="7" rx="1.5" ry="3.4" fill="none" stroke="#fff" stroke-width=".7"/>
        <path d="M3.6 7 H10.4" stroke="#fff" stroke-width=".7"/>
      </svg>
      <div class="item contact web">www.hallbrookvane.org</div>
    </footer>

    <div class="band"></div>
  </main>
</body>
</html>
```